Distillery needs label designs for unique craft rums.

Kelmoor Distillery is a premium craft distillery based in Western Cape, South Africa. We are one of the few distilleries doing cold distillation of alcohol and have developed a range of South African rums that require labels. The range consists of a Silver, Dark and Spiced Rum. We are looking for one design with thee variants as described above. The design should be modern and not "traditional" as most rum labels are.
The labels sizes are for 375ml bottles and are 80mm - height x 170mm - long.
Attached is a conceptual text label showing the regulatory requirements for the back portion (volume, abv, batch number...etc). Attached is a sample label of rums of the same variants.

Please include the following for each label:
Silver Rum: "Hint of toffee and caramel"
Dark Rum: "Bold oak aroma with undertone of vanilla"
Spiced Rum: "Light oak with hint of cinnamon"

The rums will be sold individually and in combination in a white gift box. Attached the die-lines of the gift box. Therefore the color schemes need of the labels needs to work inside a white surrounding.

Target Market(s)

Premium craft spirit consumers

Font styles to use
Sans Serif
Script

Colors

Designer to choose colors to be used in the design.

Requirements
Must have
• Reference to cold distilled
• Regulatory information on label as per sample provided
Nice to have
• None
Should not have
• No pictures i.e. ships, pirates, people etc.

```html
<!DOCTYPE html>
<html lang="en">
<head>
<meta charset="utf-8">
<title>Kelmoor Distillery – Spiced Rum Label</title>
<link rel="stylesheet" href="https://fonts.googleapis.com/css2?family=Cinzel:wght@400;700&family=Meddon&family=Oswald:wght@400;500&family=Roboto+Condensed:wght@400;500&display=swap">
<style>
  :root {
    --white: #ffffff;
    --cane-grey: #4a4a4c;
    --rum-brown: #523125;
    --spice-orange: #b86536;
    --frame: #8a8a8a;
  }
  html, body { margin: 0; padding: 0; overflow: hidden; background: var(--white); }
  .canvas {
    position: relative; width: 1200px; height: 1000px; overflow: hidden;
    background: var(--white);
  }
  .sheet-frame {
    position: absolute; left: 0; top: 0; width: 1196px; height: 996px;
    border: 1px solid var(--frame);
  }
  .label {
    position: absolute; left: 69px; top: 245px; width: 1060px; height: 499px;
    background: var(--rum-brown); overflow: hidden;
  }
  .cane-backdrop {
    position: absolute; inset: 0;
    background:
      linear-gradient(90deg,
        rgba(74,74,76,0) 0%, rgba(74,74,76,.55) 12%, rgba(74,74,76,.15) 22%,
        rgba(74,74,76,.5) 32%, rgba(74,74,76,0) 40%, rgba(74,74,76,0) 60%,
        rgba(74,74,76,.6) 66%, rgba(74,74,76,.2) 72%, rgba(74,74,76,.55) 80%,
        rgba(74,74,76,.1) 86%);
  }
  .edge-trim {
    position: absolute; left: 0; width: 100%; height: 10px;
    background: var(--spice-orange); opacity: .75;
  }
  .edge-trim--top { top: 4px; }
  .edge-trim--bottom { top: 482px; }
  .label-art { position: absolute; inset: 0; }
  .story {
    position: absolute; left: 22px; top: 48px; height: 405px; width: 78px;
    writing-mode: vertical-rl; transform: rotate(180deg);
    font-family: "Oswald", sans-serif; font-weight: 500; font-size: 11.5px;
    line-height: 18px; letter-spacing: 0.9px; color: var(--white);
    text-transform: uppercase; text-align: left;
  }
  .front {
    position: absolute; left: 381px; top: 40px; width: 300px;
    text-align: center; color: var(--white);
  }
  .brand-mark {
    display: block; width: 22px; height: 22px; margin: 14px auto 8px;
    border-radius: 50%; background: var(--white);
  }
  .brand-name {
    font-family: "Cinzel", serif; font-weight: 700; font-size: 24px;
    line-height: 28px; letter-spacing: 2px; color: var(--white); margin: 0;
  }
  .cold-distilled {
    font-family: "Cinzel", serif; font-weight: 400; font-size: 15px;
    letter-spacing: 3px; margin: 30px 0 0;
  }
  .variant-script {
    font-family: "Meddon", cursive; font-size: 44px; line-height: 56px;
    color: var(--spice-orange); margin: 14px 0 0;
  }
  .rum-title {
    font-family: "Cinzel", serif; font-weight: 400; font-size: 66px;
    line-height: 64px; margin: -6px 0 0; letter-spacing: 2px;
  }
  .tasting-note {
    font-family: "Meddon", cursive; font-size: 15px; line-height: 21px;
    color: var(--spice-orange); margin: 8px 0 0;
  }
  .origin {
    font-family: "Roboto Condensed", sans-serif; font-weight: 500; font-size: 12.5px;
    line-height: 20px; letter-spacing: 2.6px; text-transform: uppercase; margin: 12px 0 0;
  }
  .swatches { position: absolute; top: 805px; left: 68px; display: flex; gap: 21px; }
  .swatch { width: 78px; height: 72px; box-sizing: border-box; }
  .swatch--white { background: var(--white); border: 2px solid #333; }
  .swatch--grey { background: var(--cane-grey); }
  .swatch--brown { background: var(--rum-brown); }
  .swatch--orange { background: var(--spice-orange); }
</style>
</head>
<body>
<div class="canvas">
  <div class="sheet-frame"></div>

  <section class="label" aria-label="Kelmoor Distillery Spiced Rum label">
    <div class="cane-backdrop" role="img" aria-label="Grey sugarcane silhouettes rising across the label background"></div>
    <div class="edge-trim edge-trim--top" role="img" aria-label="Decorative orange edge trim"></div>
    <div class="edge-trim edge-trim--bottom" role="img" aria-label="Decorative orange edge trim"></div>

    <svg class="label-art" width="1060" height="499" viewBox="0 0 1060 499">
      <rect class="edge-line" x="0" y="21" width="1060" height="2" fill="#b86536"/>
      <rect class="edge-line" x="0" y="25" width="1060" height="2" fill="#b86536"/>
      <rect class="edge-line" x="0" y="472" width="1060" height="2" fill="#b86536"/>
      <rect class="edge-line" x="0" y="476" width="1060" height="2" fill="#b86536"/>

      <rect class="batch-box" x="863" y="117" width="100" height="118" fill="#ffffff"/>
      <g font-family="Oswald, sans-serif" fill="#ffffff">
        <text transform="translate(883 455) rotate(-90)" font-size="11" font-weight="500">SMALL BATCH DISTILLED RUM</text>
        <text transform="translate(896 455) rotate(-90)" font-size="7.5">PRODUCED AND BOTTLED IN SOUTH AFRICA</text>
        <text transform="translate(928 440) rotate(-90)" font-size="12" font-weight="500">43% ALC./VOL.</text>
        <text transform="translate(928 353) rotate(-90)" font-size="12" font-weight="500">375 ml</text>
      </g>
      <rect class="batch-rule" x="906" y="281" width="4" height="186" rx="2" fill="#ffffff"/>
      <rect class="batch-bar" x="941" y="283" width="22" height="70" fill="#ffffff"/>
      <rect class="lot-box" x="939" y="418" width="24" height="37" fill="none" stroke="#ffffff" stroke-width="1.5"/>
      <text transform="translate(955 451) rotate(-90)" font-family="Oswald, sans-serif" font-size="9" fill="#ffffff">A1632</text>
      <rect class="warning-box" x="968" y="116" width="47" height="342" fill="none" stroke="#ffffff" stroke-width="2"/>
      <text transform="translate(997 453) rotate(-90)" font-family="Oswald, sans-serif" font-size="13.5" font-weight="500" fill="#ffffff">WARNING: ALCOHOL ABUSE IS DANGEROUS TO YOUR HEALTH</text>
    </svg>

    <p class="story">Our hand crafted, small-batch distilled rum brings together innovative method, the finest locally sourced molasses and dedication to produce a distinguished rum worthy of your enjoyment</p>

    <div class="front">
      <span class="brand-mark"></span>
      <p class="brand-name">Kelmoor<br>Distillery</p>
      <p class="cold-distilled">Cold Distilled</p>
      <p class="variant-script">Spiced</p>
      <h1 class="rum-title">RUM</h1>
      <p class="tasting-note">Light Oak with a<br>Hint of Cinnamon</p>
      <p class="origin">Distilled &amp; Bottled<br>in South Africa by<br>Kelmoor Distillery</p>
    </div>
  </section>

  <div class="swatches">
    <div class="swatch swatch--white"></div>
    <div class="swatch swatch--grey"></div>
    <div class="swatch swatch--brown"></div>
    <div class="swatch swatch--orange"></div>
  </div>
</div>
</body>
</html>
```